Design a single page Shopify store web page

We are looking to have a page designed for a single page Shopify store with 2 products. We already have a basic structure that we like, though we are open to suggestions. We are looking for somebody to provide a design/color scheme that we can then implement using Shopify's templating system. We can handle the implementation(HTML / CSS / jS) as we already have 2 web developers on the team, but have not been able to find a design we liked.

The job would consist of providing a mockup (photoshop or otherwise) and any vector graphics you choose to create for the site (we can provide product photos and other images).

You can also look at http://brickwellgoods.com.au for some of our design direction we have used so far

Target Market(s)

Young Australian Males (18 - 49)

Industry/Entity Type

Store

Number of Pages Required

1 page

Font styles to use
Serif
Sans Serif

Requirements
Must have
• Single Page Design
• E-commerce Product Purchase
• Manly (whatever interpretation of that you have)

```html
<!DOCTYPE html>
<html lang="en">
<head>
<meta charset="utf-8">
<title>Brickwell Goods – Underwear &amp; Socks Subscription</title>
<link href="https://fonts.googleapis.com/css2?family=Yanone+Kaffeesatz:wght@300;400;600;700&family=Open+Sans:wght@400;600&display=swap" rel="stylesheet">
<style>
:root{
  --ink:#0b0b0b;
  --night:#151515;
  --charcoal:#1d1d1d;
  --steel:#4d7191;
  --steel-line:#8fb1cb;
  --steel-dot:#c3d7e6;
  --plans-blue:#4b7ca3;
  --go-green:#8dc641;
  --pale-blue:#e4eff8;
  --white:#ffffff;
  --grey-text:#8a8a8a;
  --light-text:#d7e3ec;
}
*{box-sizing:border-box;margin:0;padding:0}
html,body{width:1200px;height:4286px;overflow:hidden;background:var(--ink)}
body{position:relative;font-family:"Open Sans",Arial,sans-serif;color:var(--white)}
.display{font-family:"Yanone Kaffeesatz","Arial Narrow",sans-serif}
.abs{position:absolute}

/* hero */
.hero{left:0;top:0;width:1200px;height:579px;background:radial-gradient(ellipse 420px 520px at 560px 260px,#7a7a7a 0%,#4a4a4a 40%,#1e1e1e 80%,#111 100%)}
.hero-brand{left:90px;top:70px;font-size:92px;line-height:80px;font-weight:600;color:var(--white)}
.social{top:20px;width:44px;height:44px;background:var(--white);border-radius:4px}
.hero-tagline{right:34px;top:288px;width:560px;text-align:right;font-size:50px;line-height:52px;font-weight:600;font-family:"Yanone Kaffeesatz","Arial Narrow",sans-serif}
.slider-dots{left:540px;top:548px;display:flex;gap:14px}
.slider-dots span{width:18px;height:18px;border:2px solid var(--white);border-radius:50%}
.slider-dots span.on{background:var(--white)}

/* nav */
.nav{left:0;top:579px;width:1200px;height:128px;background:var(--ink)}
.nav-brand{left:78px;top:24px;font-size:52px;line-height:42px;font-weight:600}
.nav-links{left:356px;top:42px;display:flex;gap:54px;font-size:21px}
.nav-links a{color:var(--white);text-decoration:none;padding-bottom:8px}
.nav-links a.current{border-bottom:3px solid var(--white)}
.btn{background:var(--go-green);color:var(--white);text-align:center;border-radius:4px}
.nav-cta{left:968px;top:34px;width:166px;height:56px;line-height:56px;font-size:22px;font-weight:600}

/* how it works */
.how{left:0;top:707px;width:1200px;height:579px;background:var(--steel)}
.section-title{width:1200px;left:0;text-align:center;font-size:64px;font-weight:400}
.timeline{left:0;top:150px;width:1200px;height:4px;background:var(--steel-line)}
.timeline-dot{top:138px;width:28px;height:28px;border-radius:50%;background:var(--steel-dot);border:4px solid var(--steel-line)}
.step-icon{top:212px;width:160px;height:160px;border-radius:50%;background:#f3f3f3;border:8px solid #c9d7e2;display:flex;align-items:center;justify-content:center}
.step-title{top:412px;width:300px;text-align:center;font-size:24px;font-weight:600}
.step-text{top:452px;width:230px;text-align:center;font-size:16px;line-height:22px;color:var(--light-text)}

/* plans */
.plans{left:0;top:1286px;width:1200px;height:1414px;background:var(--white)}
.plans .section-title{color:var(--plans-blue);top:40px}
.product-photo{left:193px;width:398px;height:378px;border-radius:4px}
.thumb{width:58px;height:58px;border-radius:2px}
.product-name{left:737px;font-size:62px;font-weight:300;color:var(--plans-blue);letter-spacing:2px}
.product-text{left:737px;width:270px;font-size:15px;line-height:22px;color:var(--grey-text)}
.product-price{left:737px;font-size:34px;font-weight:400;color:var(--plans-blue)}
.buy{left:737px;width:250px;height:62px;line-height:62px;font-size:36px;font-weight:600;font-family:"Yanone Kaffeesatz","Arial Narrow",sans-serif}
.perks{left:201px;top:1170px;width:442px;height:201px;background:var(--pale-blue);border-radius:4px;padding:22px 24px}
.perks li{list-style:none;display:flex;align-items:center;gap:10px;font-size:22px;line-height:38px;color:#4a5b6a}

/* instagram */
.insta{left:0;top:2700px;width:1200px;height:729px;background:var(--charcoal)}
.insta .section-title{top:40px}
.insta-tile{top:141px;width:266px;height:502px}
.arrow{top:360px}

/* faq */
.faq{left:0;top:3429px;width:1200px;height:801px;background:var(--ink)}
.faq .section-title{top:12px}
.faq-item{width:250px}
.faq-item h3{font-size:22px;line-height:28px;font-weight:600;margin-bottom:10px}
.faq-item p{font-size:14px;line-height:20px;color:#a8a8a8}

/* footer */
.footer{left:0;top:4230px;width:1200px;height:56px;background:var(--ink);border-top:2px solid #3a3a3a}
.footer-brand{left:196px;top:2px;font-size:28px;line-height:24px;font-weight:600}
.footer-copy{right:196px;top:20px;font-size:12px;color:#777}
</style>
</head>
<body>

<header class="abs hero" role="img" aria-label="Photo of a muscular man's torso wearing black briefs">
</header>
<div class="abs hero-brand display">Brickwell<br>Goods</div>
<span class="abs social" style="left:1080px"></span>
<span class="abs social" style="left:1134px"></span>
<p class="abs hero-tagline">Automate your Life<br>New Underwear and<br>Socks<br>Delivered to your door<br>when you NEED it</p>
<div class="abs slider-dots"><span class="on"></span><span></span><span></span><span></span></div>

<nav class="abs nav">
  <div class="abs nav-brand display">Brickwell<br>Goods</div>
  <div class="abs nav-links">
    <a class="current" href="#how">How it works</a>
    <a href="#plans">Plans</a>
    <a href="#faq">FAQ</a>
    <a href="#about">About us</a>
  </div>
  <a class="abs btn nav-cta">Sign up now!</a>
</nav>

<section class="abs how" id="how">
  <h2 class="abs section-title display" style="top:40px">How it works</h2>
  <div class="abs timeline"></div>
  <span class="abs timeline-dot" style="left:307px"></span>
  <span class="abs timeline-dot" style="left:586px"></span>
  <span class="abs timeline-dot" style="left:873px"></span>

  <div class="abs step-icon" style="left:241px">
    <svg width="70" height="70" viewBox="0 0 70 70"><path d="M12 58 L16 42 L48 10 L60 22 L28 54 Z" fill="#666"/><path d="M12 58 L16 42 L28 54 Z" fill="#999"/></svg>
  </div>
  <div class="abs step-icon" style="left:520px">
    <svg width="70" height="70" viewBox="0 0 70 70"><circle cx="35" cy="39" r="24" fill="none" stroke="#666" stroke-width="6"/><rect x="29" y="6" width="12" height="8" fill="#666"/><path d="M35 39 L35 24 M35 39 L46 44" stroke="#666" stroke-width="5" stroke-linecap="round"/></svg>
  </div>
  <div class="abs step-icon" style="left:807px">
    <svg width="70" height="70" viewBox="0 0 70 70"><path d="M35 8 L60 21 L60 49 L35 62 L10 49 L10 21 Z M10 21 L35 34 L60 21 M35 34 L35 62" fill="none" stroke="#666" stroke-width="5" stroke-linejoin="round"/></svg>
  </div>

  <h3 class="abs step-title" style="left:171px">Choose a Plan</h3>
  <h3 class="abs step-title" style="left:450px">Choose How Often</h3>
  <h3 class="abs step-title" style="left:737px">Get your Pack</h3>
  <p class="abs step-text" style="left:206px">Lorem ipsum dolor sit amet, consectetur adipiscing elit. Autem eveniet vel tempore consequuntur.</p>
  <p class="abs step-text" style="left:485px">Lorem ipsum dolor sit amet, consectetur adipiscing elit. Autem eveniet vel tempore consequuntur.</p>
  <p class="abs step-text" style="left:772px">Lorem ipsum dolor sit amet, consectetur adipiscing elit. Autem eveniet vel tempore consequuntur.</p>
</section>

<section class="abs plans" id="plans">
  <h2 class="abs section-title display">Plans</h2>

  <div class="abs product-photo" style="top:158px;background:linear-gradient(180deg,#1d9ccf 0%,#2bb0dc 55%,#7a5634 100%)" role="img" aria-label="Photo of blue trunks laid on a wooden floor"></div>
  <div class="abs thumb" style="left:201px;top:548px;background:linear-gradient(#2aa6d6,#6d4a2c)" role="img" aria-label="Thumbnail of blue trunks"></div>
  <div class="abs thumb" style="left:272px;top:548px;background:linear-gradient(#8a6a4a,#3a2a1e)" role="img" aria-label="Thumbnail of trunks detail"></div>
  <h3 class="abs product-name display" style="top:198px">COMFORT</h3>
  <p class="abs product-text" style="top:282px">Lorem ipsum dolor sit amet, consectetur adipiscing elit. Autem eveniet vel tempore consequuntur. Officia eos, enim quasi eque earum dolore numquam possimus alias esse nulla illo.</p>
  <p class="abs product-price" style="top:420px">30.00 usd</p>
  <a class="abs btn buy" style="top:501px">Get it Now!</a>

  <div class="abs product-photo" style="top:673px;background:linear-gradient(135deg,#5a3b24 0%,#2a3a6a 40%,#c9a12e 60%,#3b2a1e 100%)" role="img" aria-label="Photo of striped and dotted socks on a wooden floor"></div>
  <div class="abs thumb" style="left:201px;top:1063px;background:linear-gradient(#2a3a6a,#5a3b24)" role="img" aria-label="Thumbnail of socks"></div>
  <div class="abs thumb" style="left:272px;top:1063px;background:linear-gradient(#c9a12e,#3b2a1e)" role="img" aria-label="Thumbnail of socks detail"></div>
  <h3 class="abs product-name display" style="top:712px">STYLE</h3>
  <p class="abs product-text" style="top:798px">Lorem ipsum dolor sit amet, consectetur adipiscing elit. Autem eveniet vel tempore consequuntur. Officia eos, enim quasi eque earum dolore numquam possimus alias esse nulla illo.</p>
  <p class="abs product-price" style="top:934px">30.00 usd</p>
  <a class="abs btn buy" style="top:1015px">Get it Now!</a>

  <ul class="abs perks">
    <li><svg width="18" height="18" viewBox="0 0 18 18"><path d="M2 9 L7 14 L16 3" fill="none" stroke="#2f9e44" stroke-width="3"/></svg>Free shipping</li>
    <li><svg width="18" height="18" viewBox="0 0 18 18"><path d="M2 9 L7 14 L16 3" fill="none" stroke="#2f9e44" stroke-width="3"/></svg>Easy Return</li>
    <li><svg width="18" height="18" viewBox="0 0 18 18"><path d="M2 9 L7 14 L16 3" fill="none" stroke="#2f9e44" stroke-width="3"/></svg>Cancel Whenever</li>
    <li><svg width="18" height="18" viewBox="0 0 18 18"><path d="M2 9 L7 14 L16 3" fill="none" stroke="#2f9e44" stroke-width="3"/></svg>Satisfaction Guaranteed</li>
  </ul>
</section>

<section class="abs insta">
  <h2 class="abs section-title display">Whats up on our Instagram</h2>
  <div class="abs insta-tile" style="left:197px;background:linear-gradient(180deg,#d8d8d8,#8a8a8a 60%,#e6e6e6)" role="img" aria-label="Black and white photo of a man in briefs"></div>
  <div class="abs insta-tile" style="left:470px;background:linear-gradient(180deg,#6a4a30 0%,#b08a54 35%,#2c3f72 60%,#c9a12e 100%)" role="img" aria-label="Photo of underwear and socks packs"></div>
  <div class="abs insta-tile" style="left:743px;background:linear-gradient(180deg,#5a3a2a 0%,#8a5a3a 35%,#2a4a8a 60%,#d0a830 100%)" role="img" aria-label="Photo of patterned socks"></div>
  <svg class="abs arrow" style="left:124px" width="26" height="46" viewBox="0 0 26 46"><path d="M22 4 L4 23 L22 42" fill="none" stroke="#fff" stroke-width="5"/></svg>
  <svg class="abs arrow" style="left:1054px" width="26" height="46" viewBox="0 0 26 46"><path d="M4 4 L22 23 L4 42" fill="none" stroke="#fff" stroke-width="5"/></svg>
</section>

<section class="abs faq" id="faq">
  <h2 class="abs section-title display">FAQ</h2>
  <div class="abs faq-item" style="left:214px;top:112px"><h3>What is Brickwell Goods?</h3><p>Lorem ipsum dolor sit amet, consectetur adipiscing elit. Autem eveniet vel tempore consequuntur. Officia eos, enim quasi eque earum possimus.</p></div>
  <div class="abs faq-item" style="left:493px;top:112px"><h3>Return Policy</h3><p>Lorem ipsum dolor sit amet, consectetur adipiscing elit. Autem eveniet vel tempore consequuntur. Officia eos, enim quasi eque earum possimus.</p></div>
  <div class="abs faq-item" style="left:763px;top:112px"><h3>Shipping Policy</h3><p>Lorem ipsum dolor sit amet, consectetur adipiscing elit. Autem eveniet vel tempore consequuntur. Officia eos, enim quasi eque earum possimus.</p></div>

  <div class="abs faq-item" style="left:214px;top:300px"><h3>What do I get with my Brickwell plan?</h3><p>Lorem ipsum dolor sit amet, consectetur adipiscing elit. Autem eveniet vel tempore consequuntur. Officia eos, enim quasi eque earum possimus.</p></div>
  <div class="abs faq-item" style="left:493px;top:300px"><h3>What is your Satisfaction Guarantee?</h3><p>Lorem ipsum dolor sit amet, consectetur adipiscing elit. Autem eveniet vel tempore consequuntur. Officia eos, enim quasi eque earum possimus.</p></div>
  <div class="abs faq-item" style="left:763px;top:300px"><h3>What brands do you Stock?</h3><p>Lorem ipsum dolor sit amet, consectetur adipiscing elit. Autem eveniet vel tempore consequuntur. Officia eos, enim quasi eque earum possimus.</p></div>

  <div class="abs faq-item" style="left:214px;top:496px"><h3>What is your cancelation policy?</h3><p>Lorem ipsum dolor sit amet, consectetur adipiscing elit. Autem eveniet vel tempore consequuntur. Officia eos, enim quasi eque earum possimus.</p></div>
  <div class="abs faq-item" style="left:493px;top:496px"><h3>How does payment work?</h3><p>Lorem ipsum dolor sit amet, consectetur adipiscing elit. Autem eveniet vel tempore consequuntur. Officia eos, enim quasi eque earum possimus.</p></div>
  <div class="abs faq-item" style="left:763px;top:496px"><h3>What about sizing?</h3><p>Lorem ipsum dolor sit amet, consectetur adipiscing elit. Autem eveniet vel tempore consequuntur. Officia eos, enim quasi eque earum possimus.</p></div>
</section>

<footer class="abs footer">
  <div class="abs footer-brand display">Brickwell<br>Goods</div>
  <p class="abs footer-copy">Copyright Brickwell Goods 2014</p>
</footer>

</body>
</html>
```